Email Notification & Marketing Templates

I want to start with something like a newsletter or informational email, but i need Top Tips to Detect Phishing Scams. Something that i can send to users so they can follow it when receiving or exchanging emails. I will also need promotional items for my company that i can send to customers as well. It can be based on on our website PLVORIX.COM

Will also need:
newsletters
announcements
marketing emails
alerts
security notifications

Examples:Items such as Security Awareness Poster Series
Phishing Awareness
Password Security
Email Attachments
QR Code scams
Public WiFi safety

```html
<!DOCTYPE html>
<html lang="en">
<head>
<meta charset="utf-8">
<title>Plvorix – Password Security Email</title>
<link href="https://fonts.googleapis.com/css2?family=Questrial&display=swap" rel="stylesheet">
<style>
:root{
  --ink:#1f2328;
  --muted:#5c6166;
  --panel-border:#d9dde1;
  --band:#f1f3f5;
  --card:#f3f5f7;
  --green:#2f9a2c;
  --green-dark:#237a1f;
  --blue:#3d8fd6;
  --red:#e04848;
  --icon-grey:#6b6f73;
  --teal:#3f8f8a;
  --chip:#e9ecee;
}
*{box-sizing:border-box;margin:0;padding:0}
html,body{width:1200px;height:462px;overflow:hidden;background:#fff}
body{position:relative;font-family:"Questrial",sans-serif;color:var(--ink)}
.email-panel{position:absolute;top:0;height:462px;background:#fff;border:1px solid var(--panel-border);border-radius:8px;overflow:hidden}
.email-panel--intro{left:1px;width:578px;border-top-left-radius:8px}
.email-panel--tips{left:600px;width:599px;border-top:none;border-top-left-radius:0;border-top-right-radius:0}
.abs{position:absolute}
.brand{left:30px;top:30px;display:flex;align-items:center;gap:10px}
.brand__mark{width:22px;height:22px;background:var(--green)}
.brand__name{font-size:44px;color:var(--green);letter-spacing:1px;line-height:1}
.hero-band{left:0;top:113px;width:100%;height:171px;background:var(--band)}
.hero-title{left:31px;top:160px;font-size:32px;line-height:36px}
.hero-art{left:310px;top:119px;width:246px;height:165px;border-radius:6px;
  background:radial-gradient(ellipse at 50% 55%,rgba(86,196,120,.55),rgba(61,143,214,.25) 45%,rgba(241,243,245,0) 72%)}
.tips-band{left:0;top:0;width:100%;height:25px;background:var(--band)}
.tips-art{left:150px;top:0;width:120px;height:22px;
  background:radial-gradient(ellipse at 50% 0%,rgba(86,196,120,.5),rgba(241,243,245,0) 70%)}
.pw-bar{height:38px;border-radius:7px;display:flex;align-items:center;padding-left:16px;font-size:21px;color:#fff}
.pw-bar--weak{background:linear-gradient(90deg,var(--red),#e7a2a2 60%,#e3e6ea);border:1px solid #c99}
.pw-bar--strong{background:linear-gradient(90deg,#45a832,#5bb04a 55%,var(--blue))}
.pw-chip{height:23px;border-radius:5px;background:var(--chip);color:#7a8086;font-size:18px;letter-spacing:2px;display:flex;align-items:center;justify-content:center;padding-top:5px}
.pw-chip--strong{background:#d9efe4;color:var(--teal)}
.pw-label{font-size:17px;text-align:center}
.divider{left:30px;top:441px;width:520px;height:2px;background:#eceff1}
.tip-card{top:227px;width:163px;height:140px;background:var(--card);border-radius:8px;display:flex;flex-direction:column;align-items:center;justify-content:flex-end;padding-bottom:22px;text-align:center;font-size:17px;line-height:21px}
.tip-card__icon{position:absolute;top:22px;left:50%;transform:translateX(-50%)}
.symbols{font-size:20px;line-height:22px;color:var(--green);font-weight:700;text-align:center}
.cta{left:163px;top:395px;width:267px;height:46px;border-radius:4px;background:linear-gradient(180deg,#3aa32f,var(--green-dark));color:#fff;font-size:19px;display:flex;align-items:center;justify-content:center}
</style>
</head>
<body>

<section class="email-panel email-panel--intro">
  <div class="abs brand"><span class="brand__name">PLVORIX</span><span class="brand__mark"></span></div>
  <div class="abs hero-band"></div>
  <h1 class="abs hero-title" style="font-weight:400">Strengthen Your<br>Passwords Today</h1>
  <div class="abs hero-art" role="img" aria-label="Illustration of a padlock with a password field on a glowing circuit board"></div>

  <svg class="abs" style="left:42px;top:315px" width="24" height="24" viewBox="0 0 24 24"><path d="M3 3L21 21M21 3L3 21" stroke="var(--icon-grey)" stroke-width="3" stroke-linecap="round"/></svg>
  <div class="abs pw-bar pw-bar--weak" style="left:30px;top:345px;width:213px;color:var(--ink)">Old123</div>
  <div class="abs pw-label" style="left:30px;top:392px;width:213px">Weak and Predictable</div>

  <svg class="abs" style="left:288px;top:315px" width="32" height="24" viewBox="0 0 32 24"><path d="M3 12L12 21L29 3" fill="none" stroke="var(--teal)" stroke-width="3.5" stroke-linecap="round" stroke-linejoin="round"/></svg>
  <div class="abs pw-bar pw-bar--strong" style="left:287px;top:345px;width:213px">Tr@!n$P@$$w0rd!^</div>
  <div class="abs pw-chip pw-chip--strong" style="left:422px;top:327px;width:64px">****</div>
  <div class="abs pw-label" style="left:287px;top:392px;width:213px">Complex and Secure</div>

  <div class="abs divider"></div>
</section>

<section class="email-panel email-panel--tips">
  <div class="abs tips-band"></div>
  <div class="abs tips-art" role="img" aria-label="Lower edge of the padlock illustration"></div>

  <svg class="abs" style="left:31px;top:76px" width="30" height="30" viewBox="0 0 30 30"><path d="M3 3L27 27M27 3L3 27" stroke="var(--icon-grey)" stroke-width="3.5" stroke-linecap="round"/></svg>
  <div class="abs pw-bar pw-bar--weak" style="left:36px;top:99px;width:229px;height:51px;color:#fff">Old123</div>
  <div class="abs pw-chip" style="left:163px;top:82px;width:72px;height:28px">****</div>
  <div class="abs pw-label" style="left:36px;top:162px;width:229px">Weak and Predictable</div>

  <svg class="abs" style="left:309px;top:76px" width="40" height="28" viewBox="0 0 40 28"><path d="M3 15L13 25L37 3" fill="none" stroke="var(--teal)" stroke-width="4" stroke-linecap="round" stroke-linejoin="round"/></svg>
  <div class="abs pw-bar pw-bar--strong" style="left:322px;top:99px;width:230px;height:51px">Tr@!n$P@$$w0rd!^</div>
  <div class="abs pw-chip pw-chip--strong" style="left:456px;top:82px;width:72px;height:28px">****</div>
  <div class="abs pw-label" style="left:322px;top:162px;width:230px">Complex and Secure</div>

  <div class="abs tip-card" style="left:26px">
    <svg class="tip-card__icon" width="104" height="30" viewBox="0 0 104 30"><path d="M2 5H102M2 5l5-3M2 5l5 3M102 5l-5-3M102 5l-5 3" stroke="var(--blue)" stroke-width="1.5" fill="none"/><rect x="2" y="16" width="100" height="12" rx="4" fill="#cfe3f1"/><rect x="2" y="16" width="76" height="12" rx="4" fill="var(--green)"/><path d="M12 18v5M22 18v5M32 18v5M42 18v5M52 18v5M62 18v5M72 18v5" stroke="#fff" stroke-width="1.2"/></svg>
    Use at least 12<br>characters
  </div>
  <div class="abs tip-card" style="left:218px">
    <div class="tip-card__icon symbols">#£*<br>×,!@</div>
    Include special<br>symbols (#,!,@)
  </div>
  <div class="abs tip-card" style="left:407px">
    <svg class="tip-card__icon" width="34" height="58" viewBox="0 0 34 58" style="top:16px"><rect x="2" y="2" width="30" height="54" rx="5" fill="#fff" stroke="var(--green)" stroke-width="3"/><rect x="7" y="16" width="20" height="10" rx="2" fill="#d9efe4" stroke="var(--teal)"/><text x="17" y="24.5" font-size="8" text-anchor="middle" fill="var(--teal)">***</text><rect x="12" y="32" width="10" height="10" fill="var(--green)"/></svg>
    Enable 2FA for<br>total security
  </div>

  <div class="abs cta">Secure Your Account</div>
</section>

</body>
</html>
```